Property risk and finance brokerage company needs a business card design

Tarlow Financial requires a business card design. Please integrate existing logo (refer uploaded file).
hex codes used on logo #002649 #008ED6 #444F51 #ADAFAA
font used - Cinzel
Contact information
Renata Sollisford
Director
Mobile: 0491 738 205
email: r.sollisford@tarlowfinancial.example.au
website: www.tarlowfinancial.example.au
CRN : 918354
PO Box 527
Kellbrook, Easthaven, 3199
Horizontal orientation please
Finance

```html
<!DOCTYPE html>
<html lang="en">
<head>
<meta charset="utf-8">
<title>Tarlow Financial – Business Card</title>
<link href="https://fonts.googleapis.com/css2?family=Open+Sans:wght@300;400&display=swap" rel="stylesheet">
<style>
  :root {
    --navy: #002649;
    --bright-blue: #008ED6;
    --slate: #444F51;
    --silver: #ADAFAA;
    --sky-top: #9fd6f6;
    --sky-mid: #2f6fb0;
    --sky-low: #8cc8ee;
    --mist-top: #a6d0d6;
    --mist-low: #5f7f87;
    --stage: #e9ecee;
    --ink-light: #ffffff;
  }
  * { box-sizing: border-box; margin: 0; padding: 0; }
  html, body { width: 1200px; height: 857px; overflow: hidden; }
  body {
    background: var(--stage);
    font-family: "Open Sans", Arial, sans-serif;
    font-weight: 300;
  }
  .card-sheet {
    position: relative;
    width: 1200px;
    height: 857px;
    display: flex;
    align-items: center;
    justify-content: center;
    gap: 60px;
  }
  .card {
    position: relative;
    width: 520px;
    height: 297px;
    overflow: hidden;
    border-radius: 3px;
    box-shadow: 0 6px 18px rgba(0, 0, 0, 0.18);
  }

  /* Front */
  .card--front {
    background: linear-gradient(180deg,
      var(--sky-top) 0%,
      #93cbef 38%,
      var(--sky-mid) 56%,
      #5d9ed8 72%,
      var(--sky-low) 82%,
      #2c6aa8 100%);
  }
  .brand-lockup {
    position: absolute;
    top: 92px;
    left: 0;
    right: 0;
    display: flex;
    align-items: center;
    justify-content: center;
    gap: 12px;
  }
  .brand-dot {
    width: 30px;
    height: 30px;
    border-radius: 50%;
    background: var(--bright-blue);
  }
  .brand-name {
    font-size: 30px;
    font-weight: 400;
    color: var(--navy);
    letter-spacing: 1px;
  }
  .website {
    position: absolute;
    right: 16px;
    bottom: 12px;
    display: flex;
    align-items: center;
    gap: 6px;
    font-size: 12px;
    color: var(--ink-light);
  }

  /* Back */
  .card--back {
    background: linear-gradient(180deg,
      var(--mist-top) 0%,
      #9cc6cc 45%,
      #82a7ae 75%,
      var(--mist-low) 100%);
  }
  .holder {
    position: absolute;
    top: 22px;
    left: 26px;
  }
  .holder-name {
    font-size: 26px;
    color: var(--ink-light);
    line-height: 1.1;
  }
  .holder-title {
    display: inline-block;
    margin-top: 4px;
    padding: 2px 10px;
    background: var(--slate);
    color: var(--ink-light);
    font-size: 11px;
  }
  .contact-list {
    position: absolute;
    top: 106px;
    left: 26px;
    width: 250px;
    list-style: none;
  }
  .contact-item {
    display: flex;
    align-items: center;
    gap: 8px;
    padding: 5px 0 6px;
    border-bottom: 1px solid rgba(255, 255, 255, 0.45);
    font-size: 11px;
    color: var(--ink-light);
    white-space: nowrap;
  }
  .contact-item:last-child { border-bottom: none; }
  .contact-icon { width: 11px; height: 11px; flex: none; }
  .brand-mark-area {
    position: absolute;
    right: 50px;
    bottom: 20px;
    width: 150px;
    height: 150px;
    border-radius: 50%;
    background: radial-gradient(circle at 40% 40%, #3b8fd6, var(--navy));
    opacity: 0.85;
  }
</style>
</head>
<body>
<main class="card-sheet">

  <section class="card card--front" aria-label="Card front">
    <div class="brand-lockup">
      <span class="brand-dot"></span>
      <span class="brand-name">Tarlow Financial</span>
    </div>
    <div class="website">
      <svg class="contact-icon" viewBox="0 0 12 12" aria-hidden="true">
        <circle cx="6" cy="6" r="5" fill="none" stroke="#fff" stroke-width="1"/>
        <ellipse cx="6" cy="6" rx="2.2" ry="5" fill="none" stroke="#fff" stroke-width="0.8"/>
        <line x1="1" y1="6" x2="11" y2="6" stroke="#fff" stroke-width="0.8"/>
      </svg>
      www.tarlowfinancial.example.au
    </div>
  </section>

  <section class="card card--back" aria-label="Card back">
    <div class="holder">
      <div class="holder-name">Renata Sollisford</div>
      <div class="holder-title">Managing Director</div>
    </div>
    <ul class="contact-list">
      <li class="contact-item">
        <svg class="contact-icon" viewBox="0 0 12 12" aria-hidden="true"><rect x="3" y="1" width="6" height="10" rx="1" fill="#444F51"/></svg>
        0491 738 205
      </li>
      <li class="contact-item">
        <svg class="contact-icon" viewBox="0 0 12 12" aria-hidden="true"><circle cx="6" cy="6" r="4.5" fill="none" stroke="#444F51" stroke-width="1.5"/><circle cx="6" cy="6" r="1.6" fill="#444F51"/></svg>
        r.sollisford@tarlowfinancial.example.au
      </li>
      <li class="contact-item">
        <svg class="contact-icon" viewBox="0 0 12 12" aria-hidden="true"><path d="M6 1v10M1.7 3.5l8.6 5M1.7 8.5l8.6-5" stroke="#444F51" stroke-width="1.6"/></svg>
        nnn nnn nnn
      </li>
      <li class="contact-item">
        <svg class="contact-icon" viewBox="0 0 12 12" aria-hidden="true"><rect x="1" y="3" width="10" height="6" rx="1" fill="#444F51"/></svg>
        PO Box 527 Kellbrook, Easthaven, 3199
      </li>
    </ul>
    <div class="brand-mark-area" role="img" aria-label="Large brand mark decoration"></div>
  </section>

</main>
</body>
</html>
```